Real Estate Investor needs awesome business card design

I invest in real estate, focused on multi-family properties, and I need a business card to hand out to potential partners. I prefer simple, clean designs, but it needs to stand out, so I'd like there to be a bit of red in the design as well.

It should include this information:

Front
Dallin Pecksworth
Real Estate Investor
Direct phone: 502-867-3394
Email: dallinhpecksworth@quillmail.example
Headshot (Picture), I've uploaded a few, just pick the one you think looks best with your design. You can remove the background from the headshot image if it looks better.

Back
The back of the card's design should flow and be congruent with the front. On the back I want to put an inspirational quote or question. There will be different ones depending on the card, so I'll need the original file so I can edit it in the end.

For now, use “The Pessimist Sees Difficulty In Every Opportunity. The Optimist Sees The Opportunity In Every Difficulty.” -Barnaby Ellsworth

Target Market(s)

Investors

Industry/Entity Type

Real Estate

Contact Information for Business Card

Front
Dallin Pecksworth
Real Estate Investor

Back
The back of the card's design should flow and be congruent with the front. On the back I want to put an inspirational quote or question. There will be different ones depending on the card, so I'll need the original file so I can edit it in the end. I've uploaded some EXAMPLES of business cards with quotes on them. Don't copy but feel free to use them as inspiration.

The design will be printed on "ZIB sized" business cards
1039 x 697 pixels
with rounded corners

Font styles to use
Serif
Decorative
Script

Colors
ec1f27

Requirements
Must have
• Headshot, name, and other information in it.
• 1039 x 697 pixels
• Rounded corners
• Clean design that pops. I'm open to see any color background, including black.
• Headshots can be located here: https://www.filecrate.example/sh/8kd2wq7mzt31hvx/BBQTXP4ruf9LmQ0KhcvWx7b?dl=0
Nice to have
• It would be awesome if the design included a personal signature or monogram, but if not I'll get a personal logo developed later and the card redesigned if I think it needs it.
Should not have
• Cluttered design

```html
<!DOCTYPE html>
<html lang="en">
<head>
<meta charset="utf-8">
<title>Dallin Pecksworth – Business Card</title>
<link rel="stylesheet" href="https://fonts.googleapis.com/css2?family=Merriweather:wght@400;700&family=Roboto+Condensed:wght@700&family=Dancing+Script:wght@600&display=swap">
<style>
  :root {
    --backdrop: #e6e1d8;
    --card-dark: #1d1d1e;
    --card-mid: #3a3a3b;
    --card-glow: #5c5c5d;
    --contact-band: #2b2a2a;
    --photo-band: #232323;
    --accent-red: #ec1f27;
    --text-white: #ffffff;
    --text-soft: #d2d2d2;
    --quote-grey: #c9c9c9;
  }
  * { margin: 0; padding: 0; box-sizing: border-box; }
  html, body { width: 959px; height: 1200px; overflow: hidden; }
  body { background: var(--backdrop); position: relative; }

  .card {
    position: absolute;
    left: 75px;
    width: 796px;
    border-radius: 28px;
    overflow: hidden;
    box-shadow: 0 6px 14px rgba(0,0,0,0.35);
  }

  /* Front */
  .card-front { top: 91px; height: 481px; background: var(--contact-band); }
  .front-panel {
    position: absolute; left: 0; top: 0; width: 796px; height: 340px;
    background: radial-gradient(ellipse 300px 260px at 330px 190px, var(--card-glow) 0%, var(--card-mid) 45%, var(--card-dark) 100%);
  }
  .photo-frame {
    position: absolute; left: 430px; top: 0; width: 366px; height: 340px;
    background: linear-gradient(135deg, #3e3e3f 0%, #2c2c2d 100%);
    box-shadow: -3px 0 6px rgba(0,0,0,0.35);
  }
  .photo-band {
    position: absolute; left: 0; top: 185px; width: 100%; height: 82px;
    background: var(--photo-band);
  }
  .headshot {
    position: absolute; left: 26px; top: 8px; width: 340px; height: 332px;
    background: linear-gradient(180deg, #5f5450 0%, #4a4549 45%, #2a2f40 75%, #1f2536 100%);
  }
  .identity {
    position: absolute; right: 386px; top: 190px;
    display: flex; flex-direction: column; align-items: flex-end;
  }
  .name {
    font-family: "Merriweather", Georgia, serif;
    font-weight: 700; font-size: 22px; color: var(--text-white);
    letter-spacing: 0.3px; line-height: 1.25;
  }
  .role {
    font-family: "Merriweather", Georgia, serif;
    font-weight: 400; font-size: 20px; color: var(--text-soft);
    word-spacing: 11px; margin-top: 6px;
  }
  .contact {
    position: absolute; left: 0; right: 0; top: 397px;
    display: flex; justify-content: center; align-items: center; gap: 20px;
    font-family: "Merriweather", Georgia, serif;
    font-weight: 700; font-size: 20px; color: var(--text-white);
  }
  .contact-item { display: flex; align-items: center; gap: 6px; }
  .contact-icon { fill: none; stroke: var(--accent-red); stroke-width: 2; }

  /* Back */
  .card-back {
    top: 634px; height: 478px;
    background: radial-gradient(ellipse 380px 330px at 300px 150px, var(--card-glow) 0%, var(--card-mid) 40%, #111112 100%);
  }
  .back-strip {
    position: absolute; left: 0; top: 0; width: 122px; height: 100%;
    background: linear-gradient(90deg, #1a1a1b 0%, #2e2e2f 70%, #3b3b3c 100%);
    box-shadow: 4px 0 8px rgba(0,0,0,0.45);
  }
  .quote {
    position: absolute; left: 216px; top: 66px;
    font-family: "Roboto Condensed", "Arial Narrow", sans-serif;
    font-weight: 700; font-size: 36px; color: var(--quote-grey);
    text-transform: uppercase; line-height: 47px;
  }
  .quote .strong { color: var(--text-white); }
  .quote-mark { position: absolute; font-size: 44px; color: var(--text-white); line-height: 47px; }
  .quote-mark.open { left: -40px; top: -2px; }
  .quote-line.gap { margin-top: 7px; }
  .attribution {
    position: absolute; right: 74px; top: 388px;
    font-family: "Dancing Script", cursive;
    font-weight: 600; font-size: 24px; color: var(--text-white);
  }
</style>
</head>
<body>

<section class="card card-front">
  <div class="front-panel"></div>
  <div class="photo-frame">
    <div class="photo-band"></div>
    <div class="headshot" role="img" aria-label="Headshot photo of Dallin Pecksworth"></div>
  </div>
  <div class="identity">
    <h1 class="name">DALLIN PECKSWORTH</h1>
    <p class="role">Real Estate Investor</p>
  </div>
  <div class="contact">
    <span class="contact-item">
      <svg class="contact-icon" width="16" height="24" viewBox="0 0 16 24" aria-hidden="true">
        <rect x="1.5" y="1.5" width="13" height="21" rx="2"/>
        <line x1="6" y1="19" x2="10" y2="19"/>
      </svg>
      502-867-3394
    </span>
    <span class="contact-item">
      <svg class="contact-icon" width="26" height="18" viewBox="0 0 26 18" aria-hidden="true">
        <rect x="1.5" y="1.5" width="23" height="15" rx="1"/>
        <polyline points="1.5,1.5 13,10 24.5,1.5"/>
      </svg>
      dallinhpecksworth@quillmail.example
    </span>
  </div>
</section>

<section class="card card-back">
  <div class="back-strip"></div>
  <blockquote class="quote">
    <span class="quote-mark open">«</span>
    <div class="quote-line">The pessimist sees</div>
    <div class="quote-line strong">Difficulty</div>
    <div class="quote-line gap">In every <span class="strong">opportunity.</span></div>
    <div class="quote-line">The optimist sees</div>
    <div class="quote-line strong">The opportunity</div>
    <div class="quote-line">In every <span class="strong">difficulty.</span> <span class="strong">»</span></div>
  </blockquote>
  <p class="attribution">Barnaby Ellsworth</p>
</section>

</body>
</html>
```